Postcard Design

I am in real estate, I wish to design a "farming" tool.

I want to show a sampling of houses (files attached) with the following text:

The spring market is here and the buyers are waiting for YOU!
Order a Market Snapshot to see what homes in your neighborhood are selling for, or call today for a personal market analysis.

Order your report at: www.48213HouseDeals.com
or reach out to me directly:
Dana Pelworth
www.SettleinBrambury.com
614.382.7095
YourRealtorDana@Mailvex.com

I also attached multiple files containing logos - in multiple formats and in black or white, depending on what is easier to use.

Target Market(s)

By neighborhood. I have a list.

Industry/Entity Type

Real Estate

Requirements
Must have
• See description above

```html
<!DOCTYPE html>
<html lang="en">
<head>
<meta charset="utf-8">
<title>Spring Market Postcard – Dana Pelworth</title>
<link href="https://fonts.googleapis.com/css2?family=Roboto+Condensed:wght@400;700&family=Arimo:ital,wght@0,400;0,700;1,700&family=Libre+Baskerville:wght@400;700&display=swap" rel="stylesheet">
<style>
  :root {
    --page: #ffffff;
    --navy: #1f3f92;
    --forest: #0a4a1f;
    --band-blue: #1c2c86;
    --deep-green: #0d4a3d;
    --teal-green: #064a40;
    --alert-red: #d6262b;
    --panel-grey: #e2e6e3;
    --address-grey: #d3d8d4;
    --ink: #222222;
    --white: #ffffff;
    --tree-lilac: #8f8fd0;
    --tree-sage: #6f9a86;
  }
  * { box-sizing: border-box; margin: 0; padding: 0; }
  html, body { width: 1200px; height: 1000px; overflow: hidden; background: var(--page); }
  .canvas { position: relative; width: 1200px; height: 1000px; }
  .serif { font-family: "Libre Baskerville", Georgia, serif; }
  .sans { font-family: "Arimo", Arial, sans-serif; }
  .cond { font-family: "Roboto Condensed", "Arial Narrow", sans-serif; }

  /* ---------- Front of postcard ---------- */
  .card-front {
    position: absolute; left: 232px; top: 22px; width: 623px; height: 483px;
    background: linear-gradient(90deg, var(--navy) 0%, #0f4560 55%, var(--forest) 100%);
    box-shadow: 6px 6px 8px rgba(0,0,0,.35);
    z-index: 2; overflow: hidden; color: var(--white);
  }
  .front-headline {
    position: absolute; top: 38px; width: 100%; text-align: center;
    font-size: 19.5px; font-weight: 400; letter-spacing: .1px;
  }
  .tree-mark { position: absolute; opacity: .75; }
  .tree-left { left: 14px; top: 82px; width: 116px; height: 222px;
    background: radial-gradient(ellipse at 50% 40%, var(--tree-lilac) 0%, rgba(143,143,208,.5) 55%, transparent 72%); }
  .tree-right { left: 492px; top: 82px; width: 124px; height: 222px;
    background: radial-gradient(ellipse at 50% 40%, var(--tree-sage) 0%, rgba(111,154,134,.5) 55%, transparent 72%); }
  .photo-grid {
    position: absolute; left: 132px; top: 70px; width: 358px; height: 234px;
    background: var(--white); padding: 4px;
    display: grid; grid-template-columns: 1fr 1fr; grid-template-rows: 1fr 1fr; gap: 4px;
  }
  .home-photo { width: 100%; height: 100%; }
  .home-a { background: linear-gradient(180deg, #9bb6d6 0%, #c9c9c3 45%, #7d8a5c 100%); }
  .home-b { background: linear-gradient(180deg, #dfe3e6 0%, #8b8a80 50%, #6f8f45 100%); }
  .home-c { background: linear-gradient(180deg, #6ea3d8 0%, #b7a88a 50%, #5b6c48 100%); }
  .home-d { background: linear-gradient(180deg, #d7e4ef 0%, #c9c2b1 50%, #6d8b46 100%); }
  .offer-band {
    position: absolute; left: 0; top: 303px; width: 100%; height: 60px;
    background: var(--band-blue); text-align: center; font-size: 15.5px; line-height: 23px; padding-top: 7px;
  }
  .offer-band b { font-weight: 700; font-size: 16.5px; }
  .front-footer {
    position: absolute; left: 0; top: 363px; width: 100%; height: 120px;
    background: linear-gradient(90deg, #0f4a45 0%, var(--deep-green) 60%, #0b3f2a 100%);
  }
  .report-bar {
    position: absolute; right: 0; top: 6px; width: 370px; height: 21px;
    background: linear-gradient(90deg, rgba(214,38,43,0) 0%, var(--alert-red) 30%);
    text-align: right; padding-right: 44px; font-size: 12.5px; line-height: 21px;
  }
  .report-bar strong { font-family: "Arimo", Arial, sans-serif; font-style: italic; font-weight: 700; font-size: 15px; }
  .agent-name {
    position: absolute; left: 30px; top: 30px; display: flex; align-items: center; gap: 10px;
  }
  .agent-name .square { width: 26px; height: 26px; background: var(--white); }
  .agent-name .name { font-size: 23px; line-height: 26px; }
  .agent-name .firm { font-size: 9px; letter-spacing: 2.2px; line-height: 14px; }
  .contact {
    position: absolute; right: 44px; top: 38px; text-align: right;
  }
  .contact .lead { font-size: 11px; line-height: 14px; }
  .contact .phone-line { font-size: 14px; line-height: 19px; }
  .contact .links { font-size: 11.5px; font-style: italic; font-weight: 700; line-height: 16px; }

  /* ---------- Back of postcard ---------- */
  .card-back {
    position: absolute; left: 328px; top: 494px; width: 622px; height: 483px;
    background: var(--panel-grey);
    box-shadow: 6px 6px 8px rgba(0,0,0,.35);
    z-index: 1; overflow: hidden;
  }
  .back-header {
    position: absolute; left: 0; top: 11px; width: 468px; height: 143px;
    background: var(--teal-green); color: var(--white);
    display: flex; align-items: center; gap: 16px; padding-left: 40px;
  }
  .back-header .square { width: 44px; height: 44px; background: var(--white); }
  .back-header .name { font-size: 38px; line-height: 44px; }
  .back-header .firm { font-size: 12px; letter-spacing: 3.2px; margin-top: 2px; }
  .postage-area {
    position: absolute; left: 468px; top: 11px; width: 154px; height: 143px;
    display: flex; align-items: center; justify-content: center; text-align: center;
    font-size: 17px; line-height: 23px; color: var(--ink);
  }
  .feature-photo {
    position: absolute; left: 0; top: 156px; width: 301px; height: 180px;
    background: linear-gradient(180deg, #8fb2d9 0%, #d6d3c6 40%, #b9a98c 62%, #5e7048 100%);
  }
  .back-report {
    position: absolute; left: 0; top: 336px; width: 301px; height: 62px;
    background: var(--teal-green); text-align: center; padding-top: 8px;
  }
  .back-report .lead { color: var(--white); font-size: 17px; line-height: 22px; }
  .back-report .url { color: var(--alert-red); font-size: 17px; font-style: italic; font-weight: 700; line-height: 24px; }
  .address-area {
    position: absolute; left: 301px; top: 156px; width: 321px; height: 242px;
    background: var(--address-grey); color: var(--ink);
  }
  .address-area h2 { font-weight: 400; font-size: 17.5px; text-align: center; margin-top: 38px; }
  .address-area p { font-size: 13px; line-height: 16px; margin: 27px 0 0 34px; width: 250px; }
  .corner-mark {
    position: absolute; left: 0; top: 398px; width: 77px; height: 85px; background: var(--teal-green);
  }
  .corner-mark .tree-mark { left: 6px; top: 8px; width: 64px; height: 64px;
    background: radial-gradient(circle at 50% 45%, var(--tree-sage) 0%, transparent 68%); }
  .barcode-area {
    position: absolute; left: 77px; top: 398px; width: 545px; height: 85px;
    display: flex; align-items: center; justify-content: center; font-size: 17px; color: var(--ink);
  }
</style>
</head>
<body>
<main class="canvas">

  <section class="card-front cond" aria-label="Postcard front">
    <h1 class="front-headline">The SPRING MARKET is here and the buyers are waiting for YOU!</h1>

    <div class="tree-mark tree-left" role="img" aria-label="Faded tree illustration"></div>
    <div class="tree-mark tree-right" role="img" aria-label="Faded tree illustration"></div>

    <div class="photo-grid">
      <div class="home-photo home-a" role="img" aria-label="Photo of a colonial house with a front lawn"></div>
      <div class="home-photo home-b" role="img" aria-label="Photo of a two-storey house with a double garage"></div>
      <div class="home-photo home-c" role="img" aria-label="Photo of a tan house with a garage and driveway"></div>
      <div class="home-photo home-d" role="img" aria-label="Photo of a light-sided house with garden shrubs"></div>
    </div>

    <div class="offer-band serif">
      <b>Order a Market Snapshot</b> to see what homes in your neighborhood<br>
      are selling for, <b>or call today</b> for a personal market analysis.
    </div>

    <div class="front-footer">
      <div class="report-bar">Order your report at: <strong>www.48213HouseDeals.com</strong></div>

      <div class="agent-name serif">
        <span class="square"></span>
        <div>
          <div class="name">Dana Pelworth</div>
          <div class="firm">HOLLOWBROOK REALTY</div>
        </div>
      </div>

      <div class="contact sans">
        <div class="lead">or reach out to me directly:</div>
        <div class="phone-line">Dana Pelworth: 614.382.7095</div>
        <div class="links">www.SettleinBrambury.com; YourRealtorDana@Mailvex.com</div>
      </div>
    </div>
  </section>

  <section class="card-back" aria-label="Postcard back">
    <header class="back-header serif">
      <span class="square"></span>
      <div>
        <div class="name">Dana Pelworth</div>
        <div class="firm">HOLLOWBROOK REALTY</div>
      </div>
    </header>

    <div class="postage-area sans">Postage<br>Area</div>

    <div class="feature-photo" role="img" aria-label="Photo of a two-storey house with garage under a blue sky"></div>

    <div class="back-report">
      <div class="lead cond">Order your report at:</div>
      <div class="url sans">www.48213HouseDeals.com</div>
    </div>

    <div class="address-area sans">
      <h2>Address Area</h2>
      <p>The only text allowed in the Address Area is the recipient mailing address. Red zones may have no text or graphics darker than 7% grayscale.</p>
    </div>

    <div class="corner-mark">
      <div class="tree-mark" role="img" aria-label="Faded tree illustration"></div>
    </div>

    <div class="barcode-area sans">Barcode Area</div>
  </section>

</main>
</body>
</html>
```